A Visual Masterpiece for an Optometry Practice

We are looking for a web designer to create a website for our optometry business that makes the client appreciate the gift of sight. We are looking for something clean and crisp but beautiful and compelling. Something that is unique and experiencial. So if you are up for the artistic challenge, lets journey together and create something amazing. We look forward to working with you!
Updates

I updated the source files for the logos. Thanks for letting me know that the other ones did not work. Thanks everyone!

I am extending the deadline due to the fact that there has only been a few submissions. This does not reflect the quality of the subissions, but we are looking for a larger pool to choose from. Thank you so much for your flexibility and patience. We appreciate you and the work you have done =)

Target Market(s)

This business is in Lancaster, Ohio which is mainly hosts mainly blue-colared families. We believe that a lot of times people do not come to an optometrist until something is wrong with their eyes, and we would love to change that. We want to bring awareness to how amazing the gift of sight is and want to focus on beauty, adventure and playfulness. With this being said, we want our website to be full of wonder, beauty and adventure. something that makes someone say, "check this out! This is freaking amazing!"

Industry/Entity Type

Business

Requirements
Must have
• Home Page
Location Page
Contact Page
"Register Online" Page
Philophy Page
Stories page (simular to a testimonial)

We would like it to be very user friendly and able to be updated easily by one of our nurses

also, I have uploaed source files of our logo for you to insert on each page.

If you have ideas or concepts that would include actual photos of the doctor or day to day activities, we can hire a photographer for quality images. We didnt want to do that prior to picking the designer.
Nice to have
• We would love it to feel simple but at the same time full of life. Wed love for the site to take the eye on a journey.

```html
<!DOCTYPE html>
<html lang="en">
<head>
<meta charset="utf-8">
<title>Clear Meridian Optometry</title>
<link rel="stylesheet" href="https://fonts.googleapis.com/css2?family=Source+Sans+3:wght@400;500&display=swap">
<style>
  :root {
    --page-bg: #e7e7e7;
    --brand-green: #1f6b4f;
    --nav-blue: #2b6b92;
    --panel-blue: #9dd0f0;
    --band-blue: #79b1d5;
    --band-overlay: rgba(112, 170, 210, 0.62);
    --frame: #ffffff;
    --footer-grey: #9a9a9a;
    --white: #ffffff;
  }
  * { box-sizing: border-box; margin: 0; padding: 0; }
  html, body {
    width: 1200px; height: 804px; overflow: hidden;
    background: var(--page-bg);
    font-family: "Source Sans 3", "Myriad Pro", Arial, sans-serif;
  }
  .page { position: relative; width: 1200px; height: 804px; }

  .brand {
    position: absolute; left: 151px; top: 182px;
    display: flex; align-items: center; gap: 12px;
    color: var(--brand-green); font-size: 28px; font-weight: 400;
    letter-spacing: -0.3px; text-decoration: none;
  }
  .brand-square { width: 40px; height: 40px; background: var(--panel-blue); }

  .main-nav {
    position: absolute; left: 484px; top: 198px;
    display: flex; gap: 37px;
  }
  .main-nav a { color: var(--nav-blue); font-size: 13px; text-decoration: none; }

  .hero {
    position: absolute; left: 120px; top: 253px;
    width: 958px; height: 301px;
    display: grid; grid-template-columns: 331px 331px 296px;
    border: 1px solid var(--frame); border-radius: 4px; overflow: hidden;
  }
  .tile { position: relative; }
  .tile-photo-left {
    background: linear-gradient(120deg, #6b4a3a 0%, #c99f8a 22%, #f1d9cf 45%, #f7ebe7 70%, #e9e3e1 100%);
  }
  .tile-intro { background: var(--panel-blue); color: var(--white); padding: 29px 33px 0; }
  .tile-photo-right {
    background: linear-gradient(110deg, #7fa64a 0%, #b5cf7a 18%, #d8b39a 45%, #c99478 70%, #a5b5c4 100%);
  }
  .intro-title { font-size: 13px; font-weight: 400; margin-bottom: 15px; }
  .intro-text { font-size: 12.5px; line-height: 20.8px; width: 268px; }

  .tile-band {
    position: absolute; left: 0; right: 0; bottom: 0; height: 69px;
    background: var(--band-overlay);
    color: var(--white); font-size: 13px; text-decoration: none;
    padding: 27px 0 0 31px;
  }
  .tile-intro .tile-band { background: var(--band-blue); }

  .site-footer {
    position: absolute; left: 151px; top: 645px; width: 873px;
    display: flex; justify-content: space-between;
    color: var(--footer-grey); font-size: 12.5px;
  }
  .footer-nav { display: flex; gap: 37px; }
  .footer-nav a { color: var(--footer-grey); text-decoration: none; }
</style>
</head>
<body>
<div class="page">
  <header>
    <a class="brand" href="#"><span class="brand-square"></span>clear meridian</a>
    <nav class="main-nav">
      <a href="#">Home</a>
      <a href="#">Location</a>
      <a href="#">Contact</a>
      <a href="#">Register Online</a>
      <a href="#">Philophy</a>
      <a href="#">Stories</a>
    </nav>
  </header>

  <main class="hero">
    <section class="tile tile-photo-left" role="img" aria-label="Photo of a smiling woman wearing rimless glasses, looking upward">
      <a class="tile-band" href="#">Philophy</a>
    </section>
    <section class="tile tile-intro">
      <h1 class="intro-title">Clear Meridian Optometry</h1>
      <p class="intro-text">The National Vision Care Council represents approximately 36,000 doctors of optometry, optometry students and paraoptometric assistants and technicians. Optometrists serve patients in nearly 6,500 communities across the country, and in 3,500 of those communities are the only eye doctors.</p>
      <a class="tile-band" href="#">Stories</a>
    </section>
    <section class="tile tile-photo-right" role="img" aria-label="Photo of a smiling young man wearing dark-framed glasses outdoors">
      <a class="tile-band" href="#">Register Online</a>
    </section>
  </main>

  <footer class="site-footer">
    <span>Copyright © 2012 clear meridian.</span>
    <nav class="footer-nav">
      <a href="#">Blog</a>
      <a href="#">Map View</a>
      <a href="#">Contact</a>
    </nav>
  </footer>
</div>
</body>
</html>
```